For Lease sign for Property management company in Kansas City

We need someone to take our information and design a standard for lease sign that we can put in front of each of our buildings. I would love for it to do its job of letting people know there are units available but also be unique somehow. Also the aspect ratio of the design would ideally be 4 wide by 3 tall but we open to other ideas. It will be a larger yard sign.

Target Market(s)

Potential Tenants

Industry/Entity Type

Real Estate Development

Font styles to use
Sans Serif

Requirements
Must have
• Our logo, our website (www.tollen-estates.com), our phone number (816) 247-5903.
Nice to have
• Some how say "For Lease"
Sign to be 4' wide by 3' tall
If there was a place to put the building name that would be cool but not ne
Should not have
• Nothing that I can think of

```html
<!DOCTYPE html>
<html lang="en">
<head>
<meta charset="utf-8">
<title>For Lease Sign – Tollen Estates</title>
<link rel="stylesheet" href="https://fonts.googleapis.com/css2?family=Montserrat:wght@700;800&display=swap">
<style>
  :root {
    --sign-red: #be1e2d;
    --gold: #f9ae3e;
    --gold-edge: #d8953a;
    --phone-gold: #f3a33b;
    --band-white: #ffffff;
    --band-blush: #f5e2da;
    --url-cream: #f7e6df;
    --page: #ffffff;
  }
  html, body {
    margin: 0;
    padding: 0;
    width: 880px;
    height: 1200px;
    overflow: hidden;
    background: var(--page);
  }
  .lease-sign {
    position: absolute;
    left: 40px;
    top: 300px;
    width: 800px;
    height: 600px;
    display: block;
  }
  .sign-text {
    font-family: "Montserrat", Arial, sans-serif;
    text-anchor: middle;
  }
  .headline { font-weight: 800; font-size: 150px; fill: var(--gold); }
  .phone { font-weight: 800; font-size: 104px; fill: var(--phone-gold); }
  .website { font-weight: 700; font-size: 54px; fill: var(--url-cream); letter-spacing: 1px; }
  .brand-name { font-weight: 800; font-size: 58px; fill: var(--sign-red); }
</style>
</head>
<body>
  <svg class="lease-sign" viewBox="0 0 1110 832" xmlns="http://www.w3.org/2000/svg" aria-label="For lease sign">
    <rect class="sign-field" width="1110" height="832" fill="var(--sign-red)"/>

    <!-- ribbon band across the middle -->
    <polygon class="ribbon" fill="var(--band-white)"
      points="0,319 555,372 1110,317 1110,512 555,465 0,512"/>
    <polygon class="ribbon-tail-left" fill="var(--band-blush)"
      points="0,319 28,322 190,512 0,512"/>
    <polygon class="ribbon-tail-right" fill="var(--band-blush)"
      points="922,335 1110,317 1110,512 1084,509"/>

    <text class="sign-text headline" x="555" y="170">FOR LEASE</text>

    <!-- brand mark: plain circle with company name -->
    <circle class="brand-disc" cx="555" cy="416" r="200"
      fill="var(--gold)" stroke="var(--gold-edge)" stroke-width="5"/>
    <text class="sign-text brand-name" x="555" y="405">TOLLEN</text>
    <text class="sign-text brand-name" x="555" y="470">ESTATES</text>

    <text class="sign-text phone" x="555" y="722">(816) 247-5903</text>
    <text class="sign-text website" x="555" y="794">WWW.TOLLEN-ESTATES.COM</text>
  </svg>
</body>
</html>
```